Criação de Kit Layout de Posts para Redes Sociais (Facebook, Instagram e etc) para Marketing & Comunicação
" somos uma empresa de audiovisual focado no mercado corporativo "

```html
<!DOCTYPE html>
<html lang="en">
<head>
<meta charset="UTF-8">
<title>Vivid Frame – Social Post</title>
<link rel="stylesheet" href="https://fonts.googleapis.com/css2?family=Montserrat:wght@400;700;900&display=swap">
<style>
  :root {
    --gold: #d9a630;
    --gold-light: #f6dc8a;
    --gold-dark: #8a5a12;
    --ink: #0b0b0c;
    --paper: #e9e9ea;
    --stage-deep: #0c1c33;
    --stage-mid: #2f6ea8;
    --stage-glow: #9cc9ee;
    --white: #ffffff;
    --camera: #1b1c1f;
  }
  * { margin: 0; padding: 0; box-sizing: border-box; }
  html, body { width: 1200px; height: 1200px; overflow: hidden; background: var(--ink); }
  .post {
    position: relative;
    width: 1200px;
    height: 1200px;
    overflow: hidden;
    font-family: "Montserrat", sans-serif;
  }
  .post__art { position: absolute; inset: 0; width: 1200px; height: 1200px; }
  .brand {
    position: absolute;
    left: 28px;
    top: 40px;
    display: flex;
    align-items: center;
    gap: 20px;
  }
  .brand__dot {
    width: 86px; height: 86px; border-radius: 50%;
    background: var(--gold);
  }
  .brand__name {
    font-weight: 700;
    font-size: 46px;
    letter-spacing: 1px;
    color: #262626;
  }
  .headline {
    position: absolute;
    left: 132px;
    top: 325px;
    font-weight: 900;
    font-size: 100px;
    line-height: 0.98;
    color: var(--ink);
    letter-spacing: 1px;
  }
  .dots {
    position: absolute;
    left: 214px;
    top: 542px;
    display: flex;
    gap: 14px;
  }
  .dots span {
    width: 16px; height: 12px;
    background: var(--gold);
  }
  .body-copy {
    position: absolute;
    left: 58px;
    top: 880px;
    width: 470px;
    font-size: 27px;
    line-height: 1.32;
    color: var(--white);
  }
  .social {
    position: absolute;
    left: 56px;
    top: 1070px;
    display: flex;
    align-items: center;
    gap: 14px;
  }
  .social__icon {
    width: 54px; height: 54px; border-radius: 50%;
    background: var(--white);
  }
  .social__handle {
    margin-left: 18px;
    font-size: 29px;
    color: var(--white);
  }
</style>
</head>
<body>
<div class="post">
  <svg class="post__art" viewBox="0 0 500 500" preserveAspectRatio="none">
    <defs>
      <radialGradient id="stageLight" cx="0.45" cy="0.42" r="0.7">
        <stop offset="0" stop-color="var(--stage-glow)"/>
        <stop offset="0.45" stop-color="var(--stage-mid)"/>
        <stop offset="1" stop-color="var(--stage-deep)"/>
      </radialGradient>
      <linearGradient id="goldBand" x1="0" y1="0" x2="1" y2="0">
        <stop offset="0" stop-color="var(--gold-dark)"/>
        <stop offset="0.45" stop-color="var(--gold-light)"/>
        <stop offset="1" stop-color="var(--gold)"/>
      </linearGradient>
      <linearGradient id="screenLight" x1="0" y1="0" x2="0" y2="1">
        <stop offset="0" stop-color="#5fa8e6"/>
        <stop offset="0.6" stop-color="#bfe1fb"/>
        <stop offset="1" stop-color="#0f2440"/>
      </linearGradient>
    </defs>

    <rect class="stage-photo" role="img" aria-label="Blurred photo of a band performing on a blue-lit stage" x="0" y="0" width="500" height="500" fill="url(#stageLight)"/>

    <polygon class="top-corner" points="0,0 500,0 500,12 0,100" fill="var(--ink)"/>
    <polygon class="top-panel" points="0,0 420,0 0,82" fill="var(--paper)"/>
    <polygon class="top-band" points="0,82 420,0 500,0 500,8 0,104" fill="url(#goldBand)"/>

    <rect class="camera-body" x="252" y="116" width="205" height="130" rx="8" fill="var(--camera)"/>
    <rect class="camera-screen" role="img" aria-label="Camera viewfinder showing a band performing live on stage" x="272" y="127" width="172" height="100" fill="url(#screenLight)"/>

    <polygon class="lower-panel" points="0,232 300,392 330,500 0,500" fill="var(--ink)"/>
    <polygon class="lower-band" points="0,218 318,386 300,396 0,236" fill="url(#goldBand)"/>
    <polygon class="corner-panel" points="500,330 500,500 330,500" fill="#cfcfd1"/>

    <ellipse class="gold-ring" cx="385" cy="395" rx="118" ry="92" fill="none" stroke="url(#goldBand)" stroke-width="34"/>
    <ellipse class="ring-inner" cx="385" cy="395" rx="96" ry="72" fill="none" stroke="var(--gold-dark)" stroke-width="6"/>
  </svg>

  <div class="brand">
    <span class="brand__dot"></span>
    <span class="brand__name">VIVID FRAME</span>
  </div>

  <h1 class="headline">LOREN<br>IPSUN</h1>
  <div class="dots"><span></span><span></span><span></span><span></span><span></span><span></span></div>

  <p class="body-copy">Lorem ipsum dolor sit amet, consectetur adipiscing elit sed do eiusmod tempor incididunt</p>

  <div class="social">
    <span class="social__icon"></span>
    <span class="social__icon"></span>
    <span class="social__icon"></span>
    <span class="social__handle">your_account</span>
  </div>
</div>
</body>
</html>
```